Need Letterhead Design & Matching Business Card

I have a logo that I love already. But the letterhead is less than appealing and boring. I'd like a design for my letterhead which I will match with business cards. Also, I'd like to have used fonts that are generally available, as my current letterhead uses a font named "SPACE" which nobody has unless they download it...so when a Word version is forwarded, it looks awful on the receiver's screed due to not having the font. That being said, modern is the look we like and are going for.

My business is "Halloran Brightmoor PC" - a law firm specializing in representing people who have suffered catastrophic injuries or death (plane, auto, train crashes etc.).

See attached letterhead, which has all of the pertinent information. My logo is also attached in various formats.

```html
<!DOCTYPE html>
<html lang="en">
<head>
<meta charset="utf-8">
<title>Halloran Brightmoor PC — Letterhead</title>
<link href="https://fonts.googleapis.com/css2?family=Montserrat:wght@300;600;700&family=Open+Sans:wght@400;600;700&family=Great+Vibes&display=swap" rel="stylesheet">
<style>
  :root {
    --backdrop: #dccdb4;
    --paper: #ffffff;
    --ink: #1a1a1a;
    --ink-soft: #555555;
    --ink-muted: #8a8a8a;
    --mark: #111111;
  }
  * { box-sizing: border-box; margin: 0; padding: 0; }
  html, body { width: 1200px; height: 898px; overflow: hidden; }
  body {
    background: var(--backdrop);
    font-family: "Open Sans", Arial, sans-serif;
    color: var(--ink);
  }
  .letterhead {
    position: absolute;
    left: 296px; top: 19px;
    width: 608px; height: 860px;
    background: var(--paper);
    padding: 52px 56px 0 56px;
  }
  .masthead { display: flex; align-items: flex-start; gap: 12px; }
  .mark-square { width: 54px; height: 54px; background: var(--mark); flex: none; }
  .firm { flex: 1; }
  .firm-name {
    font-family: "Montserrat", Arial, sans-serif;
    font-weight: 300; font-size: 22px; letter-spacing: 0.5px;
    line-height: 1; margin-top: 2px; text-transform: uppercase;
  }
  .firm-lines { display: flex; gap: 36px; margin-top: 6px; }
  .firm-address { font-size: 7.5px; line-height: 1.45; color: var(--ink); }
  .firm-contact { list-style: none; font-size: 7.5px; line-height: 1.45; }
  .firm-contact li { display: flex; align-items: center; gap: 6px; }
  .firm-contact svg { width: 7px; height: 7px; fill: var(--ink); }
  .date { text-align: right; font-size: 8px; color: var(--ink-muted); margin-top: 80px; }
  .recipient { margin-top: 14px; }
  .recipient-name { font-weight: 700; font-size: 14px; color: #333; }
  .recipient-details { font-size: 8.5px; line-height: 1.55; color: var(--ink-muted); margin-top: 4px; }
  .letter-body { margin-top: 40px; }
  .letter-body p {
    font-size: 8.6px; line-height: 1.78; color: var(--ink-soft);
    margin-bottom: 18px; text-align: left;
  }
  .sign-off { margin-top: 40px; }
  .signature { font-family: "Great Vibes", cursive; font-size: 22px; line-height: 1; color: var(--ink); }
  .signer-name { font-family: "Montserrat", Arial, sans-serif; font-weight: 700; font-size: 10px; letter-spacing: 0.3px; margin-top: 2px; }
  .signer-role { font-size: 8px; color: var(--ink-muted); margin-top: 2px; }
</style>
</head>
<body>
  <main class="letterhead">
    <header class="masthead">
      <div class="mark-square"></div>
      <div class="firm">
        <h1 class="firm-name">Halloran Brightmoor PC</h1>
        <div class="firm-lines">
          <address class="firm-address" style="font-style:normal">
            R. Tomas Verhoeven, Esq. | President<br>
            4420 Larkspur Ave. | suite 800<br>
            Fairhaven, CA 90410
          </address>
          <ul class="firm-contact">
            <li><svg viewBox="0 0 10 10"><path d="M0 2h10v6H0z M0 2l5 3.5L10 2" fill="none" stroke="#1a1a1a" stroke-width="1.2"/></svg>tomas@halloranbrightmoor.com</li>
            <li><svg viewBox="0 0 10 10"><circle cx="5" cy="5" r="4.3" fill="none" stroke="#1a1a1a" stroke-width="1.1"/><path d="M0.7 5h8.6M5 0.7c-2.2 2.6-2.2 6 0 8.6M5 0.7c2.2 2.6 2.2 6 0 8.6" fill="none" stroke="#1a1a1a" stroke-width="0.9"/></svg>www.halloranbrightmoor.com</li>
            <li><svg viewBox="0 0 10 10"><path d="M2 0.5l2 2.2-1 1.3c.6 1.4 1.6 2.4 3 3l1.3-1 2.2 2-1.2 1.5C4.5 9.2.8 5.5.5 1.7z"/></svg>(855) 410-2276</li>
          </ul>
        </div>
      </div>
    </header>

    <p class="date">Date, 10 September, 2030</p>

    <section class="recipient">
      <h2 class="recipient-name">Name Surname</h2>
      <p class="recipient-details">
        Senior Executive<br>
        Address goes here, Street, City, Country<br>
        contact@yourmail.com<br>
        000-987-654-321
      </p>
    </section>

    <section class="letter-body">
      <p>Lorem ipsum dolor sit amet, consectetur adipisicing elit, sed do eiusmod tempor incididunt ut labore et dolore magna aliqua. Ut enim ad minim veniam, quis nostrud exercitation ullamco laboris nisi ut aliquip ex ea commodo consequat. Duis aute irure dolor in reprehenderit in voluptate velit esse cillum dolore eu fugiat nulla pariatur. Excepteur sint occaecat cupidatat non proident, sunt in culpa qui officia deserunt mollit anim id est laborum. Sed ut perspiciatis unde omnis iste natus error sit voluptatem accusantium doloremque laudantium, totam rem aperiam, eaque ipsa quae ab illo inventore veritatis et quasi architecto beatae vitae dicta sunt explicabo. Nemo enim ipsam voluptatem quia voluptas sit aspernatur aut odit aut fugit, sed quia consequuntur magni dolores eos qui ratione voluptatem sequi nesciunt. Neque porro voluptatem sequi nesciunt. Nemo enim ipsam voluptatem quia voluptas.</p>
      <p>Lorem ipsum dolor sit amet, consectetur adipisicing elit, sed do eiusmod tempor incididunt ut labore et dolore magna aliqua. Ut enim ad minim veniam, quis nostrud exercitation ullamco laboris nisi ut aliquip ex ea commodo consequat. Duis aute irure dolor in reprehenderit in voluptate velit esse cillum dolore eu fugiat nulla pariatur. Excepteur sint occaecat cupidatat non proident, sunt in culpa qui officia deserunt mollit anim id est laborum. Sed ut perspiciatis unde omnis iste natus error sit voluptatem accusantium doloremque laudantium, totam rem aperiam, eaque ipsa quae ab illo inventore veritatis et quasi architecto beatae vitae dicta sunt explicabo. Nemo enim ipsam voluptatem quia voluptas sit aspernatur aut odit aut.</p>
      <p>Lorem ipsum dolor sit amet, consectetur adipisicing elit, sed do eiusmod tempor incididunt ut labore et dolore magna aliqua. Ut enim ad minim veniam, quis nostrud exercitation ullamco laboris nisi ut aliquip ex ea commodo consequat.</p>
    </section>

    <footer class="sign-off">
      <p class="signature">Namesurname</p>
      <p class="signer-name">NAME SURNAME</p>
      <p class="signer-role">General Manager</p>
    </footer>
  </main>
</body>
</html>
```